Business Card Design For Marketing Agnecy LVT

Need business card design for marketing agency.

Dorian Pell
President, CEO
1-555-304-2917
dorian@lumenvaletrewards.net
www.LumenValeTrewards.biz

Back Side:
Boost Sales Using Rewards, Incentives & Giveaways
Get A Free Sample Package

Target Market(s)

B2B

Industry/Entity Type

Marketing

Contact Information for Business Card

Dorian Pell
President, CEO
1-555-304-2917

Back Side:
Get A Free Sample Package

Please note that my current url is OLD DESIGN. I am working on new design and want the business card to match color themes at least on new site. Here is the demo link for new site so you can see the colors I use, etc.

http://pagekilnstudio.example/qx/dorian/lvt_final/index.html

Requirements
Must have
• Please note that my current url is OLD DESIGN. I am working on new design and want the business card to match color themes at least on new site. Here is the demo link for new site so you can see the colors I use, etc.

Nice to have

Should not have

```html
<!DOCTYPE html>
<html lang="en">
<head>
<meta charset="utf-8">
<title>LVT Business Card</title>
<link rel="stylesheet" href="https://fonts.googleapis.com/css2?family=Exo+2:wght@600&family=Michroma&family=Roboto:wght@400;500&display=swap">
<style>
  :root {
    --page: #b4b4b4;
    --card: #f1f1f1;
    --card-edge: #e4e4e4;
    --blue: #2d5aa3;
    --charcoal: #3a3a3c;
    --green: #4aa534;
    --green-shadow: #2f2f2f;
    --text: #2b2b2b;
    --white: #ffffff;
    --faint: rgba(0, 0, 0, 0.045);
  }
  * { box-sizing: border-box; margin: 0; padding: 0; }
  html, body {
    width: 1200px; height: 576px; overflow: hidden;
    background: var(--page);
    font-family: "Roboto", Arial, sans-serif;
  }
  .stage { position: relative; width: 1200px; height: 576px; }

  .card {
    position: absolute; top: 138px;
    width: 484px; height: 293px;
    background: linear-gradient(180deg, var(--white), var(--card) 60%, var(--card-edge));
    border-radius: 10px; overflow: hidden;
  }
  .card--back { left: 82px; }
  .card--front { left: 602px; }

  /* brand name block (replaces logo) */
  .brand {
    font-family: "Exo 2", "Roboto", sans-serif;
    font-weight: 600; color: var(--blue);
    display: flex; align-items: center; gap: 10px;
  }
  .brand__dot {
    width: 14px; height: 14px; border-radius: 50%;
    background: var(--blue); flex: none;
  }

  /* back side */
  .card--back .brand {
    position: absolute; top: 50px; left: 0; right: 0;
    justify-content: center; font-size: 40px; letter-spacing: 1px;
  }
  .offer {
    position: absolute; left: 64px; top: 146px; width: 358px; height: 68px;
  }
  .offer svg { position: absolute; inset: 0; }
  .offer__line {
    position: absolute; left: 0; right: 0; text-align: center; color: var(--white);
  }
  .offer__lead { top: 12px; font-size: 13px; }
  .offer__cta {
    top: 30px; font-family: "Michroma", sans-serif; font-size: 12px;
    letter-spacing: 0.5px; font-weight: 400;
  }
  .site-url {
    position: absolute; top: 240px; left: 0; right: 0;
    text-align: center; font-size: 13.5px; color: var(--text);
  }
  .site-url span { color: var(--blue); }
  .base-bar {
    position: absolute; left: 0; right: 0; bottom: 0; height: 12px; display: flex;
  }
  .base-bar__blue { flex: 1; background: var(--blue); }
  .base-bar__dark { flex: 1; background: var(--charcoal); }

  /* front side */
  .watermark {
    position: absolute; right: -20px; top: 40px;
    font-family: "Exo 2", "Roboto", sans-serif; font-weight: 600;
    font-size: 210px; line-height: 1; color: var(--faint);
  }
  .person { position: absolute; left: 27px; top: 45px; }
  .person__name {
    font-family: "Exo 2", "Roboto", sans-serif; font-weight: 600;
    font-size: 20px; color: var(--blue);
  }
  .person__title { font-size: 11.5px; color: var(--text); margin-top: 2px; }
  .card--front .brand {
    position: absolute; top: 92px; right: 36px;
    font-size: 34px; letter-spacing: 1px;
  }
  .contacts {
    position: absolute; left: 27px; top: 202px; list-style: none;
    font-size: 12px; color: var(--text);
  }
  .contacts li { display: flex; align-items: center; gap: 9px; height: 18.5px; }
  .contacts svg { width: 11px; height: 11px; fill: var(--charcoal); flex: none; }
  .front-bar {
    position: absolute; left: 0; bottom: 0; width: 260px; height: 10px;
    background: var(--charcoal);
  }
  .front-tab { position: absolute; right: 0; bottom: 0; width: 246px; height: 36px; }
  .front-tab svg { position: absolute; inset: 0; }
  .front-tab__text {
    position: absolute; left: 28px; right: 0; top: 11px; text-align: center;
    font-family: "Michroma", sans-serif; font-size: 10.5px; color: var(--white);
  }
</style>
</head>
<body>
<main class="stage">

  <section class="card card--back" aria-label="Card back">
    <div class="brand"><span class="brand__dot"></span>Lumen Vale Trewards</div>

    <div class="offer">
      <svg viewBox="0 0 358 68" preserveAspectRatio="none" aria-hidden="true">
        <polygon points="6,64 352,64 338,70 20,70" fill="var(--green-shadow)"/>
        <polygon points="0,0 358,0 352,45 200,60 158,60 6,45" fill="var(--green)"/>
      </svg>
      <p class="offer__line offer__lead">Boost Sales Using Rewards, Incentives &amp; Giveaways</p>
      <p class="offer__line offer__cta">GET A FREE SAMPLE PACKAGE</p>
    </div>

    <p class="site-url">www.<span>LumenValeTrewards</span>.biz</p>

    <div class="base-bar"><span class="base-bar__blue"></span><span class="base-bar__dark"></span></div>
  </section>

  <section class="card card--front" aria-label="Card front">
    <div class="watermark" aria-hidden="true">LVT</div>

    <div class="person">
      <h1 class="person__name">Dorian Pell</h1>
      <p class="person__title">President, CEO</p>
    </div>

    <div class="brand"><span class="brand__dot"></span>LVT</div>

    <ul class="contacts">
      <li>
        <svg viewBox="0 0 12 12" aria-hidden="true"><path d="M1 4c0-2 2-3 5-3s5 1 5 3v1H8V4H4v1H1zM3 6h6l2 3v2H1V9z"/></svg>
        1-555-304-2917
      </li>
      <li>
        <svg viewBox="0 0 12 12" aria-hidden="true"><path d="M0 2h12v8H0zM1 3l5 4 5-4v-.2H1z" fill-rule="evenodd"/></svg>
        dorian@lumenvaletrewards.net
      </li>
      <li>
        <svg viewBox="0 0 12 12" aria-hidden="true"><path d="M6 0a6 6 0 1 0 0 12A6 6 0 0 0 6 0zm0 1.2c.7 0 1.5 1.4 1.7 3.8H4.3C4.5 2.6 5.3 1.2 6 1.2zM1.3 5h1.9c0-1.3.3-2.5.7-3.3A4.8 4.8 0 0 0 1.3 5zm0 2a4.8 4.8 0 0 0 2.6 3.3C3.5 9.5 3.3 8.3 3.2 7zm3 0h3.4c-.2 2.4-1 3.8-1.7 3.8S4.5 9.4 4.3 7zm4.5 0c0 1.3-.3 2.5-.7 3.3A4.8 4.8 0 0 0 10.7 7zm1.9-2A4.8 4.8 0 0 0 8.1 1.7c.4.8.7 2 .7 3.3z"/></svg>
        LumenValeTrewards.biz
      </li>
    </ul>

    <div class="front-bar"></div>
    <div class="front-tab">
      <svg viewBox="0 0 246 36" preserveAspectRatio="none" aria-hidden="true">
        <polygon points="10,0 246,0 246,36 0,36" fill="var(--blue)"/>
      </svg>
      <p class="front-tab__text">Get A Free Sample Package</p>
    </div>
  </section>

</main>
</body>
</html>
```